Geschäftspapiere für Rechtsberatung
Zielgruppe
Rechtsberatung; Zielgruppe sind sowohl Privat- als auch Geschäftsleute
Die Einzelkanzlei von Greta Münzberg (Näheres siehe www.muenzberg-kanzlei.de) wird zu einer Partnergesellschaft, der
Münzberg

```html
<!DOCTYPE html>
<html lang="de">
<head>
<meta charset="utf-8">
<title>Briefbogen Münzberg &amp; Horstkamp</title>
<link href="https://fonts.googleapis.com/css2?family=Open+Sans:wght@400;600;700&display=swap" rel="stylesheet">
<style>
  :root {
    --brand-red: #a01008;
    --band-grey: #ababab;
    --stage: #dcdcdc;
    --paper: #ffffff;
    --ink: #1c1c1c;
    --faint: #f5f5f5;
    --on-band: #ffffff;
  }
  * { margin: 0; padding: 0; box-sizing: border-box; }
  html, body { width: 1200px; height: 968px; overflow: hidden; }
  body {
    background: var(--stage);
    font-family: "Open Sans", Arial, sans-serif;
    color: var(--ink);
    position: relative;
  }
  .letterhead {
    position: absolute;
    left: 280px; top: 31px;
    width: 640px; height: 905px;
    background: var(--paper);
    box-shadow: 0 4px 14px rgba(0,0,0,.18);
    overflow: hidden;
  }
  .band { position: absolute; left: 0; width: 640px; display: block; }
  .band--top { top: 0; height: 22px; }
  .band--bottom { bottom: 0; height: 40px; }
  .sender-line {
    position: absolute; left: 42px; top: 104px;
    font-size: 6px; letter-spacing: .1px;
    border-bottom: 0.8px solid var(--ink);
    padding-bottom: 2px; width: 212px; white-space: nowrap;
  }
  .firm-mark {
    position: absolute; left: 382px; top: 130px;
    display: flex; align-items: center; gap: 10px;
  }
  .firm-mark__dot {
    width: 26px; height: 26px; border-radius: 50%;
    background: var(--brand-red); flex: none;
  }
  .firm-mark__name {
    font-size: 17px; font-weight: 600; color: var(--brand-red);
    line-height: 1.2; white-space: nowrap;
  }
  .firm-mark__name small { display: block; font-size: 11px; letter-spacing: .6px; }
  .partners {
    position: absolute; left: 430px; top: 200px;
    border-left: 0.8px solid var(--ink);
    padding-left: 14px;
    font-size: 8.4px; line-height: 1.36;
  }
  .partners strong { font-weight: 700; display: block; }
  .partners .gap { margin-top: 3px; }
  .contact-row { display: flex; align-items: center; gap: 5px; }
  .contact-row svg { width: 8px; height: 8px; flex: none; }
  .reference {
    position: absolute; left: 350px; top: 316px;
    font-size: 8.4px; line-height: 1.36;
  }
  .watermark {
    position: absolute; left: 190px; top: 600px;
    width: 200px; height: 200px; border-radius: 50%;
    background: var(--faint);
  }
  .bank-line {
    position: absolute; left: 24px; bottom: 16px;
    font-size: 7.5px; line-height: 1; color: var(--on-band);
    white-space: nowrap; letter-spacing: .2px;
  }
  .bank-line span { margin: 0 8px; }
  .web-address {
    position: absolute; right: 22px; bottom: 8px;
    font-size: 11px; line-height: 1; color: var(--on-band); letter-spacing: 1px;
  }
</style>
</head>
<body>
  <main class="letterhead">
    <svg class="band band--top" viewBox="0 0 640 22" preserveAspectRatio="none">
      <path d="M0 0 H640 V20 H150 C138 20 136 12 124 12 H0 Z" fill="var(--band-grey)"/>
      <path d="M0 0 H640 V7 H150 C138 7 136 12 124 12 H0 Z" fill="var(--brand-red)"/>
    </svg>

    <p class="sender-line">RAe Münzberg &amp; Horstkamp | Brunnenstr. 14 | 45527 Feldhausen</p>

    <div class="firm-mark">
      <span class="firm-mark__dot"></span>
      <span class="firm-mark__name">Münzberg &amp; Horstkamp<small>Rechtsanwältinnen PartGmbB</small></span>
    </div>

    <div class="partners">
      <strong>Greta Münzberg</strong>
      Diplom-Juristin<br>
      Dozentin für Bankrecht
      <strong class="gap">Sabine Horstkamp</strong>
      Fachanwältin für Erbrecht<br>
      Fachanwältin für Familienrecht
      <div class="gap">Brunnenstraße 14<br>45527 Feldhausen</div>
      <div class="contact-row gap">
        <svg viewBox="0 0 10 10"><path d="M2 1 L4 1 L4.6 3.2 L3.4 4 C4 5.4 4.8 6.2 6 6.6 L6.8 5.4 L9 6 L9 8 C5 8.6 1.4 5 2 1 Z" fill="var(--brand-red)"/></svg>
        02301/44 28 100
      </div>
      <div class="contact-row">
        <svg viewBox="0 0 10 10"><rect x="1" y="4" width="8" height="5" fill="var(--brand-red)"/><rect x="3" y="1" width="4" height="3" fill="var(--brand-red)"/></svg>
        02301/44 28 102
      </div>
      <div class="contact-row">
        <svg viewBox="0 0 10 10"><rect x="0.5" y="2" width="9" height="6" fill="var(--brand-red)"/><path d="M0.5 2 L5 5.5 L9.5 2" stroke="#fff" stroke-width="0.8" fill="none"/></svg>
        info@muenzberg-kanzlei.de
      </div>
    </div>

    <div class="reference">Unser Zeichen:<br>Datum:</div>

    <div class="watermark" aria-hidden="true"></div>

    <svg class="band band--bottom" viewBox="0 0 640 40" preserveAspectRatio="none">
      <path d="M0 4 H440 C452 4 454 28 466 28 H0 Z" fill="var(--band-grey)"/>
      <path d="M0 28 H430 C444 28 446 8 460 8 H640 V40 H0 Z" fill="var(--brand-red)"/>
    </svg>
    <p class="bank-line">Nordkreis Bank AG<span>|</span>IBAN: DE12 3456 7800 0012 3456 78<span>|</span>BIC: NRKBDEX1XXX</p>
    <p class="web-address">www.muenzberg-kanzlei.de</p>
  </main>
</body>
</html>
```